High-end residential home builder needs a business card design

We need a new business card design for a small residential construction company based in Boise, Idaho. We specialize in building custom high-end homes and remodels, with a focus on great design and craftsmanship.

We would like to use our current logo, but open to new color suggestions.
Just looking for a clean, sharp, modern design that looks high-end.

Target Market(s)

Upscale clientele

Industry/Entity Type

Contractor

Contact Information for Business Card

Company: Stonefield Custom Builders
Name: Marcus Tilley
Phone number: 208 367 4120
Email: MarcusTilleySCB@mailbox-example.com
Website: Stonefieldcustombuilders-example.com

Font styles to use
Serif
Sans Serif

Requirements
Must have
• Company Logo
Company name
My name
My phone number
My email
Company website
Nice to have
• I have attached a few photos of cards that I really like.

```html
<!DOCTYPE html>
<html lang="en">
<head>
<meta charset="utf-8">
<title>Stonefield Custom Builders – Business Card</title>
<link href="https://fonts.googleapis.com/css2?family=Michroma&family=Open+Sans:wght@400;600&family=Raleway:wght@600;700&display=swap" rel="stylesheet">
<style>
  :root {
    --backdrop: #3b3b3b;
    --card: #ffffff;
    --brown: #3d302b;
    --orange: #e09238;
    --ink: #2f2a28;
  }
  * { box-sizing: border-box; margin: 0; padding: 0; }
  html, body { width: 1200px; height: 780px; overflow: hidden; }
  body { background: var(--backdrop); font-family: "Open Sans", Arial, sans-serif; color: var(--ink); }

  .card {
    position: absolute; left: 100px; top: 104px;
    width: 1000px; height: 572px;
    background: var(--card);
    border-radius: 28px;
    overflow: hidden;
    box-shadow: 0 18px 40px rgba(0,0,0,.35);
  }
  .card__art { position: absolute; inset: 0; width: 100%; height: 100%; }

  .brand { position: absolute; left: 70px; top: 72px; display: flex; align-items: center; gap: 24px; }
  .brand__mark { width: 90px; height: 90px; border: 4px solid var(--brown); flex: none; }
  .brand__name { font-family: "Raleway", Arial, sans-serif; font-weight: 700; text-transform: uppercase; }
  .brand__primary {
    color: var(--brown); font-size: 24px; letter-spacing: 6px; line-height: 1.2;
    padding-bottom: 6px; border-bottom: 2px solid var(--brown);
  }
  .brand__secondary {
    color: var(--orange); font-size: 14px; letter-spacing: 6px; line-height: 1.2;
    margin-top: 7px; padding-left: 22px;
  }

  .person { position: absolute; left: 580px; top: 112px; width: 270px; }
  .person__name {
    font-family: "Michroma", Arial, sans-serif; color: var(--orange);
    font-size: 18px; letter-spacing: 3px; text-transform: uppercase; line-height: 1;
    white-space: nowrap;
  }
  .person__title { font-size: 14px; color: var(--ink); margin-top: 6px; }

  .address { position: absolute; left: 70px; top: 272px; font-size: 19px; line-height: 1.4; font-style: normal; }

  .contacts { position: absolute; left: 70px; top: 372px; list-style: none; }
  .contacts li { display: flex; align-items: center; gap: 20px; height: 46px; font-size: 19px; }
  .contacts svg { width: 30px; height: 30px; flex: none; }
  .icon { fill: none; stroke: var(--orange); stroke-width: 2.2; stroke-linecap: round; stroke-linejoin: round; }
  .icon--solid { fill: var(--orange); stroke: none; }
</style>
</head>
<body>
  <article class="card">
    <svg class="card__art" viewBox="0 0 1000 572" preserveAspectRatio="none" aria-hidden="true">
      <path fill="var(--brown)" d="M780,0 C900,60 962,180 962,300 C962,400 905,490 832,572 H1000 V0 Z"/>
      <path fill="var(--orange)" d="M905,190 C938,330 902,462 762,572 H520 C720,480 862,380 905,190 Z"/>
    </svg>

    <header class="brand">
      <div class="brand__mark"></div>
      <div class="brand__name">
        <div class="brand__primary">Stonefield</div>
        <div class="brand__secondary">Custom Builders</div>
      </div>
    </header>

    <div class="person">
      <div class="person__name">Marcus Tilley</div>
      <div class="person__title">CEO/Managing Director</div>
    </div>

    <address class="address">
      1480 Ridgecrest Lane<br>Suite 210, Boise ID 83702
    </address>

    <ul class="contacts">
      <li>
        <svg viewBox="0 0 30 30"><path class="icon" d="M7 4 L11 4 L13 10 L10 12 C11.5 16 14 18.5 18 20 L20 17 L26 19 L26 23 C26 25 24 26 22 26 C12 25 5 18 4 8 C4 6 5 4 7 4 Z"/><path class="icon" d="M17 5 A8 8 0 0 1 25 13 M17 9 A4 4 0 0 1 21 13"/></svg>
        208-367-4120
      </li>
      <li>
        <svg viewBox="0 0 30 30"><rect class="icon--solid" x="8" y="3" width="14" height="7" rx="1"/><rect class="icon--solid" x="3" y="10" width="24" height="11" rx="2"/><rect x="8" y="17" width="14" height="10" fill="#fff" stroke="var(--orange)" stroke-width="2"/><path class="icon" d="M11 21 H19 M11 24 H19" stroke-width="1.5"/></svg>
        208-367-4120
      </li>
      <li>
        <svg viewBox="0 0 30 30"><rect class="icon--solid" x="3" y="7" width="24" height="16" rx="1.5"/><path d="M4 8 L15 17 L26 8" fill="none" stroke="#fff" stroke-width="1.8"/></svg>
        MarcusTilleySCB@mailbox-example.com
      </li>
      <li>
        <svg viewBox="0 0 30 30"><circle class="icon" cx="15" cy="15" r="11"/><ellipse class="icon" cx="15" cy="15" rx="5" ry="11"/><path class="icon" d="M4 15 H26 M6 9 H24 M6 21 H24"/></svg>
        www.stonefieldcustombuilders-example.com
      </li>
    </ul>
  </article>
</body>
</html>
```